Global investment holding company - Business Card Design

Brenvik Holdings is a recently incorporated investment holding company. Based in Singapore, it has operations in global emerging markets in the transport & logistics, energy and livestock industries.

Its tagline "Building Shared Futures" reflects the company's philosophy of helping countries progress through partnerships which generate employment and share benefits with its society.

We are looking for a business card that reflects our global presence - incorporating the logo design into the business card design. It must have a sophisticated, modern & corporate feel.

Target Market(s)

Investors and high level governmental officials

Industry/Entity Type

Investment

Requirements
Must have
• - Use of shades of blue in logo

-Profile picture

- Name: Dennis Okoro
- Title: Chairman
- Email: dennis@brenvikholdings.example
- Mob: +65 9154 6081
- Tel: +65 6419 5820
- DID: + 65 6419 5821
- Address: 47 Marlow Road, #05-03, Singapore 048812

- website: www.brenvikholdings.example

```html
<!DOCTYPE html>
<html lang="en">
<head>
<meta charset="utf-8">
<title>Brenvik Holdings – Business Cards</title>
<link rel="stylesheet" href="https://fonts.googleapis.com/css2?family=Open+Sans:wght@400;600;700&display=swap">
<style>
  :root {
    --backdrop: #e9e6e1;
    --card-white: #ffffff;
    --navy: #1a4a8c;
    --blue-deep: #1d5fae;
    --blue-mid: #1f86d2;
    --blue-light: #5db7e8;
    --grey-text: #5f6164;
    --ink: #2b2b2b;
    --rule: #a9abaf;
    --card-edge: #6b5a4a;
  }
  * { box-sizing: border-box; margin: 0; padding: 0; }
  html, body { width: 1200px; height: 789px; overflow: hidden; }
  body {
    background: var(--backdrop);
    font-family: "Open Sans", Arial, sans-serif;
    position: relative;
  }
  .card {
    position: absolute;
    width: 506px;
    height: 290px;
    border-radius: 20px;
    overflow: hidden;
    background: var(--card-white);
    border: 1px solid var(--card-edge);
  }
  .card--front { left: 328px; top: 56px; }
  .card--back-light { left: 60px; top: 397px; }
  .card--back-blue {
    left: 616px; top: 397px;
    border: none;
    background: radial-gradient(ellipse at 50% 40%, #3aa6e6 0%, #1f86d2 45%, #1658a8 100%);
  }
  .front-art { position: absolute; inset: 0; }
  .profile-photo {
    position: absolute;
    left: 386px; top: 128px;
    width: 112px; height: 162px;
    border-radius: 56px 56px 0 0;
    background: linear-gradient(180deg, #2f4f86 0%, #3d6aa8 45%, #24365a 80%, #1a2640 100%);
  }
  .brand {
    position: absolute;
    display: flex;
    align-items: center;
    gap: 16px;
  }
  .brand-dot {
    border-radius: 50%;
    background: var(--blue-mid);
    flex: none;
  }
  .brand-name {
    font-weight: 700;
    color: var(--navy);
    line-height: 1.02;
  }
  .front-brand { left: 26px; top: 21px; }
  .front-brand .brand-dot { width: 73px; height: 73px; }
  .front-brand .brand-name { font-size: 27px; }
  .tagline {
    position: absolute;
    color: var(--grey-text);
    letter-spacing: 1.2px;
    text-transform: uppercase;
    white-space: nowrap;
  }
  .front-tagline { left: 32px; top: 112px; font-size: 12.5px; }
  .contact {
    position: absolute;
    left: 26px;
    font-size: 11.5px;
    color: var(--ink);
    white-space: nowrap;
    display: flex;
    align-items: center;
    gap: 4px;
  }
  .contact svg { width: 10px; height: 10px; fill: var(--ink); flex: none; }
  .contact svg + svg, .contact .gap { margin-left: 4px; }
  .contact--phones { top: 140px; }
  .contact--email { top: 159px; }
  .contact--web { top: 178px; }
  .contact--address { top: 200px; }
  .person {
    position: absolute;
    right: 128px; top: 248px;
    text-align: right;
    color: #fff;
  }
  .person-name { font-size: 16px; font-weight: 700; line-height: 1.1; }
  .person-title { font-size: 13px; line-height: 1.3; }
  .back-brand { left: 116px; top: 80px; }
  .back-brand .brand-dot { width: 95px; height: 95px; }
  .back-brand .brand-name { font-size: 40px; }
  .card--back-blue .brand-dot { background: #ffffff; }
  .card--back-blue .brand-name { color: #ffffff; }
  .back-tagline {
    left: 0; right: 0; top: 198px;
    text-align: center;
    font-size: 16px;
  }
  .card--back-blue .back-tagline { color: #ffffff; }
  .back-web {
    position: absolute;
    left: 0; right: 0; top: 258px;
    text-align: center;
    font-size: 14px;
    letter-spacing: 2px;
    color: var(--ink);
  }
  .card--back-blue .back-web { color: #ffffff; }
</style>
</head>
<body>

<section class="card card--front">
  <svg class="front-art" viewBox="0 0 506 290" preserveAspectRatio="none" aria-hidden="true">
    <defs>
      <linearGradient id="frontBlue" x1="0" y1="1" x2="1" y2="0">
        <stop offset="0" stop-color="#5db7e8"/>
        <stop offset="0.45" stop-color="#1f86d2"/>
        <stop offset="1" stop-color="#1a4a8c"/>
      </linearGradient>
    </defs>
    <polygon points="440,0 506,0 506,290 360,290" fill="#1a4a8c"/>
    <polygon points="0,268 506,226 506,290 0,290" fill="url(#frontBlue)"/>
    <line x1="0" y1="258" x2="370" y2="227" stroke="var(--rule)" stroke-width="3"/>
  </svg>

  <div class="profile-photo" role="img" aria-label="Profile photo of Dennis Okoro in a dark suit"></div>

  <div class="brand front-brand">
    <span class="brand-dot"></span>
    <span class="brand-name">Brenvik<br>Holdings</span>
  </div>
  <p class="tagline front-tagline">Building Shared Futures</p>

  <p class="contact contact--phones">
    <svg viewBox="0 0 10 10"><path d="M2 0.5 L3.6 2.6 L2.8 3.6 C3.4 4.9 4.9 6.4 6.3 7.1 L7.3 6.3 L9.5 7.9 L8.4 9.5 C4.6 9.4 0.6 5.4 0.5 1.6 Z"/></svg>+65 6419 5820
    <svg class="gap" viewBox="0 0 10 10"><path d="M2 0.5 L3.6 2.6 L2.8 3.6 C3.4 4.9 4.9 6.4 6.3 7.1 L7.3 6.3 L9.5 7.9 L8.4 9.5 C4.6 9.4 0.6 5.4 0.5 1.6 Z"/></svg>+65 6419 5821(DID)
    <svg class="gap" viewBox="0 0 10 10"><path d="M2.5 0 H7.5 V10 H2.5 Z M3.3 1.2 V7.6 H6.7 V1.2 Z"/></svg>+65 9154 6081
  </p>
  <p class="contact contact--email">
    <svg viewBox="0 0 10 10"><path d="M0.5 2 H9.5 V8 H0.5 Z"/></svg>dennis@brenvikholdings.example
  </p>
  <p class="contact contact--web">
    <svg viewBox="0 0 10 10"><circle cx="5" cy="5" r="4.5"/></svg>www.brenvikholdings.example
  </p>
  <p class="contact contact--address">47 Marlow Road, #05-03, Singapore 048812</p>

  <div class="person">
    <p class="person-name">Dennis Okoro</p>
    <p class="person-title">Chairman</p>
  </div>
</section>

<section class="card card--back-light">
  <div class="brand back-brand">
    <span class="brand-dot"></span>
    <span class="brand-name">Brenvik<br>Holdings</span>
  </div>
  <p class="tagline back-tagline">Building Shared Futures</p>
  <p class="back-web">www.brenvikholdings.example</p>
</section>

<section class="card card--back-blue">
  <div class="brand back-brand">
    <span class="brand-dot"></span>
    <span class="brand-name">Brenvik<br>Holdings</span>
  </div>
  <p class="tagline back-tagline">Building Shared Futures</p>
  <p class="back-web">www.brenvikholdings.example</p>
</section>

</body>
</html>
```